Long Established Local Fencing (not swords) Business needs fresh Business Cards

We need fresh double sided business cards for our Fencing Construction business, we are looking for something with our new logo design added, and maybe a photo background ?
We recently had cards made from Cardlyne and we were horrified with what we got back, the quality was terrible, so am looking for high quality format for good printing company to make.
We install Steelmora, Timber paling, Aluminium Slat Screening, Picket (timber and aluminium) and most other fencing installations.
Our website is brankelrails.com.au should you like to learn a bit more.
We do have logo in other formats if required.
We have been in business for over 35 years and we have used this as a "motto" it is on our signage

Industry/Entity Type

Construction

Contact Information for Business Card

Open to ideas, we need 3 x different cards, one generic with no name and 2 x others each with 1 of our bosses name on each, I will put into upload files.

Colors
ec1f27
000000
606060
f5f5f5

Requirements
Must have
• Company Name and Logo
• Address
• Contact details, phone, website, email etc
• Small space to write notes when leaving card at residence
Nice to have
• Our motto "Servicing the Peninsula for over 35 years"

```html
<!DOCTYPE html>
<html lang="en">
<head>
<meta charset="utf-8">
<title>Brankel Rails – Business Cards</title>
<link href="https://fonts.googleapis.com/css2?family=Open+Sans:wght@400;600;800&display=swap" rel="stylesheet">
<style>
  :root {
    --brand-red: #ec1f27;
    --brand-red-dark: #b5161c;
    --brand-black: #151515;
    --brand-grey: #606060;
    --paper: #f5f5f5;
    --white: #ffffff;
    --backdrop: #dcdcdc;
  }
  * { box-sizing: border-box; margin: 0; padding: 0; }
  html, body {
    width: 1200px; height: 900px; overflow: hidden;
    background: var(--backdrop);
    font-family: "Open Sans", Arial, sans-serif;
  }
  .canvas { position: relative; width: 1200px; height: 900px; }

  .card {
    position: absolute;
    width: 525px; height: 300px;
    border-radius: 22px;
    overflow: hidden;
    background: var(--white);
    box-shadow: 0 10px 24px rgba(0,0,0,.22);
  }
  .card--front { left: 80px; top: 480px; }
  .card--back  { left: 595px; top: 120px; background: var(--paper); }

  .card__shapes { position: absolute; inset: 0; }

  /* front: identity */
  .identity { position: absolute; left: 30px; top: 30px; padding-left: 12px; border-left: 6px solid var(--brand-red); }
  .identity__name { color: var(--white); font-size: 22px; font-weight: 400; line-height: 1.1; white-space: nowrap; }
  .identity__licence { color: var(--brand-red); font-size: 11px; text-transform: uppercase; letter-spacing: .2px; white-space: nowrap; }

  .contacts { position: absolute; left: 30px; top: 112px; list-style: none; color: var(--white); font-size: 12px; line-height: 1.35; }
  .contacts li { display: flex; align-items: flex-start; gap: 7px; margin-bottom: 4px; white-space: nowrap; }
  .contacts svg { width: 12px; height: 12px; flex: none; margin-top: 2px; fill: var(--brand-red); }

  /* brand lockup */
  .brand { position: absolute; display: flex; align-items: center; gap: 8px; }
  .brand__dot { width: 16px; height: 16px; border-radius: 50%; background: var(--brand-red); flex: none; }
  .brand__name { font-weight: 800; font-size: 30px; letter-spacing: 1px; color: var(--brand-black); text-transform: uppercase; line-height: 1; white-space: nowrap; }
  .brand__line { display: block; }

  .card--front .brand { left: 322px; top: 92px; }
  .card--front .brand__name { font-size: 26px; line-height: 1.05; }
  .abn { position: absolute; left: 346px; top: 158px; color: var(--brand-red); font-size: 13px; font-weight: 600; white-space: nowrap; }

  .card--back .brand { left: 210px; top: 95px; }
  .website { position: absolute; left: 235px; top: 140px; color: var(--brand-red); font-size: 14px; font-weight: 600; white-space: nowrap; }
  .notes-line { position: absolute; left: 40px; width: 250px; border-top: 1.5px solid var(--brand-black); }
  .notes-line--1 { top: 205px; }
  .notes-line--2 { top: 250px; }
</style>
</head>
<body>
<main class="canvas">

  <section class="card card--front" aria-label="Business card front">
    <svg class="card__shapes" viewBox="0 0 525 300" preserveAspectRatio="none" aria-hidden="true">
      <polygon points="0,0 330,0 268,90 242,172 0,202" fill="var(--brand-black)"/>
      <polygon points="330,0 372,0 305,78 278,160 242,172 268,90" fill="var(--brand-red-dark)"/>
      <polygon points="372,0 390,0 322,70 305,78" fill="var(--brand-red)"/>
      <polygon points="0,202 242,172 196,236 120,300 0,300" fill="var(--brand-red)"/>
      <polygon points="242,172 278,160 196,236" fill="var(--brand-red-dark)"/>
    </svg>

    <div class="identity">
      <p class="identity__name">Darren Molloy</p>
      <p class="identity__licence">Gold Licence No. 52914</p>
    </div>

    <ul class="contacts">
      <li><svg viewBox="0 0 12 12"><path d="M3 0h6a1 1 0 0 1 1 1v10a1 1 0 0 1-1 1H3a1 1 0 0 1-1-1V1a1 1 0 0 1 1-1zm0 1.5v8h6v-8z"/></svg>4388 2150</li>
      <li><svg viewBox="0 0 12 12"><path d="M1 4c0-2 10-2 10 0v1H8V4H4v1H1zm2 2h6l2 5H1z"/></svg>0455 302 618</li>
      <li><svg viewBox="0 0 12 12"><path d="M0 2h12v8H0zm1 1v.4l5 3.3 5-3.3V3z"/></svg>office@brankelrails.com.au</li>
      <li><svg viewBox="0 0 12 12"><path d="M6 0a4 4 0 0 1 4 4c0 3-4 8-4 8S2 7 2 4a4 4 0 0 1 4-4zm0 2.5a1.5 1.5 0 1 0 0 3 1.5 1.5 0 0 0 0-3z"/></svg>PO Box 812<br>Harbourvale NSW 2261</li>
    </ul>

    <div class="brand">
      <span class="brand__dot"></span>
      <span class="brand__name"><span class="brand__line">Brankel</span><span class="brand__line">Rails</span></span>
    </div>
    <p class="abn">ABN 41 208 95 316</p>
  </section>

  <section class="card card--back" aria-label="Business card back">
    <div class="brand">
      <span class="brand__dot"></span>
      <span class="brand__name">Brankel Rails</span>
    </div>
    <p class="website">www.brankelrails.com.au</p>
    <div class="notes-line notes-line--1"></div>
    <div class="notes-line notes-line--2"></div>
  </section>

</main>
</body>
</html>
```